Cork Lantern website design elements

Company: Cork Lantern
Business: Wine website (selling wine online)
www.corklantern.com.au
Please note that this is an initial project, ongoing design work will be required after this project.
Design requirement
Note: Full website design not required, only specific elements to enhance current design.
- Must work with existing logo and wood background (do not change site background)
- Must work with a orange (please improve current orange colour) and blue colour (blue colour in attachments)
- Pictures of wine bottles or wine glasses are not to be used in design elements.
I currently have an existing design which I would like certain elements designed for. Design elements must work with responsive functionality.
I am trying to achieve a modern retro feel of the website, please refer to the below websites as examples that I am trying to look like.
- https://au.pennytrimguild.com/
- http://www.harveykettle.com/italian/australia/home
- http://www.marigoldfizz.co.uk/
- http://www.netgather.org.nz/13/
As mentioned the site is already built and I need certain elements to work with what is already there. All elements must work with current logo and wood panel background.
I require the following elements
• Menu bar (must be the orange)
• Home page promo slider (Text, this weeks special etc)
• 2x homepage promo tabs buttons (Join the lantern club, what's in the box deal)
• 4x Homepage navigation tabs (Red wine, White wine, Sparkling, Pre mixed cases)
• Add to cart button
• Product image backdrop (can be wider than current examples)
o I would like the backdrops to be a different colour scheme to each other e.g red wine will habe red colour, white will have a cream colour, etc)
o I would prefer a close up of the product, does not need to be full view
Please refer to attachments for elements that I like and would like to mimic.
Colour scheme
- Use existing orange (please suggest if you think of a better tone)
- Secondary colour light baby blue (suggest best options)
- Please advise of other colours needed
Design elements to be provided in jog and raw design format.
This project will require ongoing work.
I will provide access details to site upon request.
Please contact me if you have any questions.
Rowan
Cork Lantern

```html
<!DOCTYPE html>
<html lang="en">
<head>
<meta charset="utf-8">
<title>Cork Lantern</title>
<link rel="stylesheet" href="https://fonts.googleapis.com/css2?family=Bebas+Neue&family=Arimo:wght@400;700&display=swap">
<style>
:root{
  --wood-light:#e38c57;
  --wood-mid:#d6773f;
  --wood-dark:#c9682f;
  --panel:#f3f4f8;
  --orange:#f0621c;
  --nav-text:#5a5a5a;
  --blue:#5dc0d3;
  --blue-line:#e9f7fa;
  --coral:#d85c50;
  --coral-line:#f8b79a;
  --red-tab:#d42d1e;
  --peach-tab:#d9825f;
  --teal-tab:#82b9b3;
  --text:#555;
  --white:#fff;
  --badge:#d9574b;
  --badge-yellow:#ffc21c;
  --fb:#1f6db4;
  --tw:#45b4e2;
  --li:#1a7a9c;
}
*{margin:0;padding:0;box-sizing:border-box}
html,body{width:1174px;height:1200px;overflow:hidden}
body{font-family:"Arimo",Arial,sans-serif;background:var(--wood-mid)}
.wood{position:absolute;left:0;top:0;width:1174px;height:1200px;
  background:linear-gradient(90deg,var(--wood-dark) 0%,var(--wood-light) 30%,var(--wood-mid) 55%,var(--wood-light) 80%,var(--wood-dark) 100%)}
.page{position:relative;width:1100px;height:1124px;transform:scale(1.0673);transform-origin:0 0}
.abs{position:absolute}
.brand{left:100px;top:28px;font-family:"Bebas Neue",sans-serif;font-size:50px;line-height:.92;color:var(--white);letter-spacing:1px}
.cart{left:878px;top:32px;display:flex;align-items:center;gap:8px;color:var(--white);font-size:14px}
.search{left:786px;top:78px;width:217px;height:29px;background:var(--white);border:1px solid #ddd;font-size:13px;color:#777;padding:7px 11px}
.search svg{position:absolute;right:8px;top:7px}
.frame{left:88px;top:130px;width:922px;height:950px;background:rgba(255,255,255,.35);border-radius:2px}
.panel{left:98px;top:142px;width:905px;height:930px;background:var(--panel)}
.nav{left:121px;top:173px;width:862px;height:56px;border-top:4px solid var(--orange);border-bottom:4px solid var(--orange);display:flex;align-items:center}
.nav a{font-family:"Bebas Neue",sans-serif;font-size:28px;color:var(--nav-text);text-decoration:none;text-align:center;letter-spacing:.5px;border-right:1px solid #ccc;line-height:32px}
.nav a:last-child{border-right:0}
.slider{left:120px;top:272px;width:507px;height:250px;background:var(--white);padding:6px;box-shadow:0 18px 14px -12px rgba(0,0,0,.18)}
.slider .photo{width:495px;height:239px;background:radial-gradient(ellipse at 55% 60%,#a85a28 0,#5e2e10 35%,#24120a 70%,#100806 100%)}
.dots{left:549px;top:499px;display:flex;gap:4px}
.dots i{width:12px;height:12px;border-radius:50%;background:#ddd;display:block}
.dots i:first-child{background:#aaa}
.badge{left:202px;top:349px}
.promo{left:678px;width:304px;color:var(--white);font-family:"Bebas Neue",sans-serif;font-size:30px;line-height:36px;text-align:center;text-decoration:none}
.promo svg{position:absolute;left:0;top:0}
.promo .label{position:absolute;left:110px;width:180px}
.tab{top:606px;width:200px;height:151px;color:var(--white);text-align:center}
.tab .product{position:absolute;left:0;top:-26px;width:60px;height:177px}
.tab .info{position:absolute;left:60px;right:0;top:18px}
.tab h2{font-family:"Bebas Neue",sans-serif;font-weight:400;font-size:31px;line-height:36px}
.tab p{font-size:12.5px;line-height:19px;margin-top:11px}
.tab .price{font-size:20px;font-weight:700;margin-top:12px}
.tab-red{left:120px;background:linear-gradient(135deg,#e23a26,#c02314)}
.tab-red .product{background:#b02a1d}
.tab-cream{left:340px;background:linear-gradient(180deg,#fafafa,#dcdcdc);color:#666}
.tab-cream .product{background:#d6d6d6}
.tab-peach{left:563px;background:var(--peach-tab)}
.tab-peach .product{background:#c97552}
.tab-teal{left:783px;background:var(--teal-tab)}
.tab-teal .product{background:#72aaa4}
.rule{left:121px;width:860px;height:5px;background:repeating-linear-gradient(45deg,#bbb 0 1px,transparent 1px 3px)}
.contact{top:834px;display:flex;align-items:center;gap:20px;color:var(--text)}
.contact .main{font-size:14px}
.contact .sub{font-size:12px;margin-top:6px}
.sep{top:846px;width:1px;height:38px;background:#ccc}
.legal{left:151px;top:971px;font-size:12px;color:#444}
.copy{left:155px;top:1003px;font-size:12px;color:#444}
.social{top:977px;width:37px;height:37px;border-radius:50%}
</style>
</head>
<body>
<div class="wood" role="img" aria-label="Warm wood panel background"></div>
<div class="page">
  <div class="abs brand">Cork<br>Lantern</div>

  <div class="abs cart">
    <svg width="28" height="26" viewBox="0 0 28 26" fill="none" stroke="#fff" stroke-width="2"><path d="M1 2h5l4 15h13l3-10H8"/><circle cx="12" cy="22" r="2"/><circle cx="21" cy="22" r="2"/></svg>
    <span>Cart (0) items</span>
  </div>
  <div class="abs search">Search..
    <svg width="14" height="14" viewBox="0 0 14 14" fill="none" stroke="#999" stroke-width="2"><circle cx="6" cy="6" r="4.5"/><path d="M9.5 9.5l3.5 3.5"/></svg>
  </div>

  <div class="abs frame"></div>
  <div class="abs panel"></div>

  <nav class="abs nav">
    <a href="#" style="width:125px">Home</a>
    <a href="#" style="width:173px">Red Wine</a>
    <a href="#" style="width:184px">White Wine</a>
    <a href="#" style="width:182px">Sparkling</a>
    <a href="#" style="width:198px">Mixed Cases</a>
  </nav>

  <div class="abs slider"><div class="photo" role="img" aria-label="Wine cellar with rows of oak barrels"></div></div>
  <svg class="abs badge" width="116" height="116" viewBox="0 0 116 116">
    <circle cx="58" cy="58" r="56" fill="var(--badge)" stroke="var(--badge)" stroke-width="4" stroke-dasharray="3 3"/>
    <circle cx="58" cy="58" r="49" fill="none" stroke="#f0a49a" stroke-width="1.5" stroke-dasharray="3 3"/>
    <text x="58" y="46" text-anchor="middle" font-family="Bebas Neue, sans-serif" font-size="30" fill="#fff">UPTO</text>
    <text x="58" y="80" text-anchor="middle" font-family="Bebas Neue, sans-serif" font-size="31"><tspan fill="var(--badge-yellow)">25%</tspan><tspan fill="#fff">OFF</tspan></text>
  </svg>
  <div class="abs dots"><i></i><i></i><i></i><i></i></div>

  <a class="abs promo" href="#" style="top:276px;height:112px">
    <svg width="304" height="112" viewBox="0 0 304 112"><rect width="304" height="112" fill="var(--blue)"/><path d="M10 11h284M10 103h284" stroke="var(--blue-line)" stroke-width="3"/>
      <path d="M40 26h50c0 26-10 38-25 38S40 52 40 26zM65 64v22M52 90h26" fill="none" stroke="#e9f7fa" stroke-width="5"/><path d="M43 40h44c-2 14-10 21-22 21s-20-7-22-21z" fill="#e9f7fa"/></svg>
    <span class="label" style="top:21px">Join the<br>Lantern Club</span>
  </a>
  <a class="abs promo" href="#" style="top:412px;height:111px">
    <svg width="304" height="111" viewBox="0 0 304 111"><rect width="304" height="111" fill="var(--coral)"/><path d="M10 10h284M10 101h284" stroke="var(--coral-line)" stroke-width="3"/>
      <g fill="none" stroke="var(--coral-line)" stroke-width="5" stroke-linejoin="round"><path d="M38 48l28 10 28-10v32l-28 10-28-10z"/><path d="M66 58v32"/><path d="M38 48l-6-18 26 8 8 20M94 48l8-20-28 2-8 28"/></g></svg>
    <span class="label" style="top:20px">What's in the<br>Box Deal</span>
  </a>

  <div class="abs tab tab-red"><div class="product" role="img" aria-label="Product photo of a red wine"></div><div class="info"><h2>Red Wine</h2><p>Pelleque habitant<br>morb tristique senet</p><div class="price">$177.98</div></div></div>
  <div class="abs tab tab-cream"><div class="product" role="img" aria-label="Product photo of a white wine"></div><div class="info"><h2>White Wine</h2><p>Pelleque habitant<br>morb tristique senet</p><div class="price">$177.98</div></div></div>
  <div class="abs tab tab-peach"><div class="product" role="img" aria-label="Product photo of a sparkling wine"></div><div class="info"><h2>Sparkling</h2><p>Pelleque habitant<br>morb tristique senet</p><div class="price">$177.98</div></div></div>
  <div class="abs tab tab-teal"><div class="product" role="img" aria-label="Product photo of a white wine"></div><div class="info"><h2>White Wine</h2><p>Pelleque habitant<br>morb tristique senet</p><div class="price">$177.98</div></div></div>

  <div class="abs rule" style="top:803px"></div>

  <div class="abs contact" style="left:123px">
    <svg width="56" height="56" viewBox="0 0 56 56"><circle cx="28" cy="28" r="27" fill="var(--blue)" stroke="var(--blue)" stroke-width="3" stroke-dasharray="2 2"/><path d="M28 42c-7-9-10-14-10-18a10 10 0 0 1 20 0c0 4-3 9-10 18z" fill="#fff"/><circle cx="28" cy="24" r="4" fill="var(--blue)"/></svg>
    <div><div class="main">Duis autem vel eum iriureHendrerit.</div><div class="sub">Typi non habent claritatem insitam</div></div>
  </div>
  <div class="abs sep" style="left:441px"></div>
  <div class="abs contact" style="left:490px">
    <svg width="56" height="56" viewBox="0 0 56 56"><circle cx="28" cy="28" r="27" fill="var(--blue)" stroke="var(--blue)" stroke-width="3" stroke-dasharray="2 2"/><path d="M20 15l6 6-3 4c2 4 5 7 9 9l4-3 6 6-4 4c-10 0-22-12-22-22z" fill="#fff"/></svg>
    <div class="main">123 - 456 - 789</div>
  </div>
  <div class="abs sep" style="left:682px"></div>
  <div class="abs contact" style="left:734px;gap:8px">
    <svg width="56" height="56" viewBox="0 0 56 56"><circle cx="28" cy="28" r="27" fill="var(--blue)" stroke="var(--blue)" stroke-width="3" stroke-dasharray="2 2"/><rect x="15" y="19" width="26" height="18" fill="#fff"/><path d="M15 19l13 10 13-10" fill="none" stroke="var(--blue)" stroke-width="2"/></svg>
    <div class="main">info@corklantern.com</div>
  </div>

  <div class="abs rule" style="top:932px"></div>

  <div class="abs legal">Privacy Policy | Terms and Conditions</div>
  <div class="abs copy">© Copyrights 2013. All Rights Reserved.</div>
  <a class="abs social" href="#" aria-label="Social link" style="left:820px;background:var(--fb)"></a>
  <a class="abs social" href="#" aria-label="Social link" style="left:870px;background:var(--tw)"></a>
  <a class="abs social" href="#" aria-label="Social link" style="left:921px;background:var(--li)"></a>
</div>
</body>
</html>
```